Innovative Consulting Firm Needs New Business Cards and Stationary

Our Innovative Consulting Firm, Larkfield Consulting, is in need of new business cards and stationary designs. We want two-sided cards that incorporate our logo, which is attached. We are looking for something not too formal, but is professional and slick.

Card should have the following information:
Name (ex. Tom Bradley)
Title (ex. Manager)
Address (ex. 24680 Cedar Lane)
Address 2 (ex. Suite 100)
City
State
Zip Code
Mobile
Email

The card should also have our website: www.larkfieldconsulting.example

Industry/Entity Type

Management Consulting

Contact Information for Business Card

Name (ex. Tom Bradley)
Title (ex. Manager)
Address 2 (ex. Suite 100)
City
State
Zip Code
Mobile
Email

Font styles to use
Sans Serif

Requirements
Must have
• The colors on the card must match the colors in the logo. The exact color codes are attached in a pdf.
Nice to have
• The Company's Tagline is "Focused on your Future". This might be nice to incorporate, but not necessary.

```html
<!DOCTYPE html>
<html lang="en">
<head>
<meta charset="utf-8">
<title>Larkfield Consulting – Business Card</title>
<link href="https://fonts.googleapis.com/css2?family=Arimo:wght@400;700&family=Orbitron:wght@700&display=swap" rel="stylesheet">
<style>
  :root {
    --ink-blue: #1f4f7a;
    --deep-blue: #1e4a72;
    --gold: #f5b21c;
    --paper: #ffffff;
    --mist: #ebebeb;
    --stage: #000000;
  }
  * { box-sizing: border-box; margin: 0; padding: 0; }
  html, body { width: 999px; height: 1200px; overflow: hidden; background: var(--stage); }
  .canvas { position: relative; width: 999px; height: 1200px; }
  .card {
    position: absolute; left: 52px; width: 906px; height: 517px;
    background: var(--paper); overflow: hidden;
    font-family: "Arimo", Arial, sans-serif;
  }
  .card--front { top: 76px; }
  .card--back { top: 620px; }
  .card__swoosh { position: absolute; inset: 0; width: 906px; height: 517px; }

  .wordmark {
    position: absolute; display: flex; align-items: center; gap: 12px;
    font-family: "Arimo", Arial, sans-serif; font-weight: 700;
    font-size: 42px; color: var(--ink-blue); white-space: nowrap; letter-spacing: 0.5px;
  }
  .wordmark__dot { width: 18px; height: 18px; border-radius: 50%; background: var(--gold); flex: none; }
  .card--front .wordmark { left: 40px; top: 60px; }
  .card--back .wordmark { left: 50%; top: 50%; transform: translate(-50%, -50%); }

  .holder { position: absolute; left: 42px; top: 225px; }
  .holder__name {
    font-family: "Orbitron", "Arimo", sans-serif; font-weight: 700;
    font-size: 31px; color: var(--gold); letter-spacing: 1px; line-height: 1;
  }
  .holder__title { margin-top: 12px; font-size: 22px; color: var(--deep-blue); }

  .address { position: absolute; left: 42px; top: 414px; color: var(--paper); font-size: 23px; line-height: 37px; }

  .contacts { position: absolute; left: 488px; top: 337px; list-style: none; color: var(--paper); font-size: 23px; }
  .contacts__item { display: flex; align-items: center; height: 36px; }
  .contacts__icon { width: 22px; height: 22px; margin-right: 21px; flex: none; }
</style>
</head>
<body>
<main class="canvas">

  <section class="card card--front" aria-label="Card front">
    <svg class="card__swoosh" viewBox="0 0 906 517" aria-hidden="true">
      <path d="M0,352 C330,345 660,220 864,0 L906,0 L906,517 L0,517 Z" fill="var(--mist)"/>
      <path d="M0,362 C340,356 680,228 883,0 L906,0 L906,517 L0,517 Z" fill="var(--deep-blue)"/>
      <path d="M418,290 C600,230 760,120 826,0 L874,0 C760,140 600,235 418,290 Z" fill="var(--gold)"/>
    </svg>

    <div class="wordmark"><span class="wordmark__dot"></span>Larkfield Consulting</div>

    <div class="holder">
      <p class="holder__name">Tom Bradley</p>
      <p class="holder__title">Manager</p>
    </div>

    <address class="address" style="font-style:normal">
      24680 Cedar Lane)<br>
      suit # 00, Lorem ipsum
    </address>

    <ul class="contacts">
      <li class="contacts__item">
        <svg class="contacts__icon" viewBox="0 0 24 24" aria-hidden="true"><path d="M6 3l3 4-2 2c1 3 4 6 7 7l2-2 4 3-2 3C10 20 4 14 3 5z" fill="none" stroke="#fff" stroke-width="2" stroke-linejoin="round"/></svg>
        00 0000 0000
      </li>
      <li class="contacts__item">
        <svg class="contacts__icon" viewBox="0 0 24 24" aria-hidden="true"><rect x="6" y="2" width="12" height="20" rx="2" fill="none" stroke="#fff" stroke-width="2"/><line x1="10" y1="18" x2="14" y2="18" stroke="#fff" stroke-width="2"/></svg>
        0000 000 000
      </li>
      <li class="contacts__item">
        <svg class="contacts__icon" viewBox="0 0 24 24" aria-hidden="true"><path d="M2 10l10-7 10 7v11H2z" fill="#fff"/><path d="M2 10l10 7 10-7" fill="none" stroke="var(--deep-blue)" stroke-width="2"/></svg>
        hello@larkfieldconsulting.example
      </li>
      <li class="contacts__item">
        <svg class="contacts__icon" viewBox="0 0 24 24" aria-hidden="true"><g fill="none" stroke="#fff" stroke-width="1.6"><circle cx="12" cy="12" r="9"/><ellipse cx="12" cy="12" rx="4" ry="9"/><line x1="3" y1="12" x2="21" y2="12"/><path d="M5 7h14M5 17h14"/></g></svg>
        www.larkfieldconsulting.example
      </li>
    </ul>
  </section>

  <section class="card card--back" aria-label="Card back">
    <div class="wordmark"><span class="wordmark__dot"></span>Larkfield Consulting</div>
  </section>

</main>
</body>
</html>
```